Digital Business Card Design

Digital Business Card with QR Code

Target Market(s)

Corprate

Industry/Entity Type

Insurance and Finance

Contact Information for Business Card

Info included on signature block plus QR Code

Font styles to use
Other font styles liked:
• Galano Fmaily

Requirements
Should not have
• Use Color scheme of Logo

```html
<!DOCTYPE html>
<html lang="pt-BR">
<head>
<meta charset="utf-8">
<title>Vanta Seguros – Business Card</title>
<link href="https://fonts.googleapis.com/css2?family=Montserrat:wght@400;500;700;800&display=swap" rel="stylesheet">
<style>
  :root {
    --page: #ffffff;
    --card: #2d3a43;
    --teal: #3b838b;
    --white: #ffffff;
    --font: "Montserrat", sans-serif;
  }
  * { margin: 0; padding: 0; box-sizing: border-box; }
  html, body { width: 1200px; height: 1120px; overflow: hidden; background: var(--page); }
  body { position: relative; font-family: var(--font); color: var(--white); }

  .card {
    position: absolute;
    width: 697px; height: 397px;
    background: var(--card);
    border-radius: 36px;
  }
  .card-front { left: 167px; top: 122px; }
  .card-back  { left: 330px; top: 613px; }

  /* front */
  .brand {
    position: absolute; left: 0; right: 0; top: 165px;
    display: flex; flex-direction: column; align-items: center;
  }
  .brand-name {
    font-weight: 800; font-size: 68px; letter-spacing: 1px; line-height: 1;
  }
  .brand-sub {
    align-self: flex-end; margin-right: 165px; margin-top: 6px;
    font-weight: 700; font-size: 18px; letter-spacing: 7px; color: var(--teal);
  }
  .website {
    position: absolute; left: 0; right: 0; top: 346px;
    text-align: center; font-size: 12px; letter-spacing: 5px; font-weight: 400;
  }

  /* back */
  .brand-mark {
    position: absolute; left: 70px; top: 212px;
    display: flex; align-items: center; gap: 12px;
  }
  .brand-mark .dot { width: 22px; height: 22px; border-radius: 50%; background: var(--teal); }
  .brand-mark .word { font-weight: 800; font-size: 44px; letter-spacing: 1px; }

  .person { position: absolute; left: 321px; top: 92px; width: 306px; }
  .person-name { font-weight: 500; font-size: 38px; line-height: 1.1; }
  .person-title { font-size: 14px; margin-top: 2px; }
  .divider { position: relative; height: 2px; background: var(--teal); margin-top: 12px; opacity: .85; }
  .divider::before { content: ""; position: absolute; left: 0; top: -1px; width: 76px; height: 3px; background: var(--teal); }

  .contacts { position: absolute; left: 321px; top: 217px; list-style: none; font-size: 15.5px; font-weight: 500; }
  .contacts li { display: flex; align-items: flex-start; gap: 14px; margin-bottom: 8px; line-height: 19px; }
  .contacts svg { width: 14px; height: 16px; flex: none; margin-top: 2px; fill: var(--teal); }
  .contacts li.address { margin-top: 12px; }
</style>
</head>
<body>

<section class="card card-front">
  <div class="brand">
    <span class="brand-name">VANTA</span>
    <span class="brand-sub">SEGUROS</span>
  </div>
  <p class="website">www.vantaseguros.com.br</p>
</section>

<section class="card card-back">
  <div class="brand-mark">
    <span class="dot"></span>
    <span class="word">VANTA</span>
  </div>

  <div class="person">
    <h1 class="person-name">Daniel Moura</h1>
    <p class="person-title">Chief Executive Officer</p>
    <div class="divider"></div>
  </div>

  <ul class="contacts">
    <li>
      <svg viewBox="0 0 14 16" aria-hidden="true"><rect x="3" y="1" width="8" height="14" rx="2"/><rect x="5" y="3" width="4" height="4" fill="#2d3a43"/></svg>
      +1.(555).210.0184
    </li>
    <li>
      <svg viewBox="0 0 14 16" aria-hidden="true"><path d="M3 2l3 0 1 3-2 1.5c.8 2 2 3.2 4 4L10.5 8.5l3 1v3c-6 .5-11-4.5-10.5-10.5z"/></svg>
      +55.(11).5550.1290
    </li>
    <li>
      <svg viewBox="0 0 14 16" aria-hidden="true"><path d="M1 4h12v9H1z M2 5l5 4 5-4" fill="none" stroke="#3b838b" stroke-width="1.2"/></svg>
      daniel@vantaseguros.com.br
    </li>
    <li class="address">
      <svg viewBox="0 0 14 16" aria-hidden="true"><path d="M7 1a5 5 0 0 1 5 5c0 3.5-5 9-5 9S2 9.5 2 6a5 5 0 0 1 5-5z"/><circle cx="7" cy="6" r="1.8" fill="#2d3a43"/></svg>
      <span>Rua das Acácias, 1450, 3º andar,<br>Vila Serena, SP, 04500-100</span>
    </li>
  </ul>
</section>

</body>
</html>
```